New Flyer Design Project

PAGE 1

Change to 8th Annual Ridgeback Clash and the new date is January 24, 2026

12U, Middle School & High School - add Open 18+

Under Weigh-ins
Early Registration is $25.00
Deadline is January 18, 2026 at 11:59 PM

Regular Registration is $35.00
Deadline is January 21, 2026 at 11:59 PM

Late / On-site Registration is $50.00
Deadline is January 23, 2026 at 5:00 PM
Change 500 to 750

Under Weigh-Ins - Change
January 24, 2025 to January 23, 2026
January 25, 2025 to January 24, 2026

PAGE 2
Change 2024-2025 to 2025-2026

In the Division Line Fix the numbers 1, 2, 3, 4, 5, 6, 7, 8, 9, 10

Change 12/31/2024 to 12/31/2025 where it says "Age As Of"
Change to "Excluding the High School & Open Division"

```html
<!DOCTYPE html>
<html lang="en">
<head>
<meta charset="utf-8">
<title>8th Annual Ridgeback Clash – Flyer</title>
<link href="https://fonts.googleapis.com/css2?family=Anton&family=Oswald:wght@400;500;600&display=swap" rel="stylesheet">
<style>
:root{
  --stage:#8f8f8f;
  --parchment:#f3ece4;
  --parchment-edge:#e4d6c8;
  --maroon:#6b1518;
  --maroon-deep:#4a0d10;
  --brown:#8a5a2b;
  --brown-dark:#6b4220;
  --peach:#f4c89a;
  --gold:#d78a2a;
  --ribbon:#b07a34;
  --cream:#f7e6cf;
  --ink:#2b1a10;
  --pill:#5e0f12;
  --table-line:#f3dcc0;
}
*{box-sizing:border-box;margin:0;padding:0}
html,body{width:1200px;height:896px;overflow:hidden;background:var(--stage)}
body{position:relative;font-family:"Oswald",sans-serif;font-variant:small-caps}
.page{position:absolute;top:66px;width:510px;height:722px;overflow:hidden;background:linear-gradient(180deg,var(--parchment),var(--parchment-edge));box-shadow:0 2px 6px rgba(0,0,0,.35)}
.page--front{left:84px}
.page--back{left:628px}
.page > *{z-index:3}
.page > .band,.page > .panel,.page > .peach,.page > .bottom{z-index:1}
.page > .art{z-index:2}
.title{position:absolute;font-family:"Anton",sans-serif;font-weight:400;font-variant:small-caps;color:var(--gold);line-height:1;white-space:nowrap;text-align:center;text-shadow:1px 1px 0 #4a2a10,2px 2px 2px rgba(0,0,0,.3)}
.front-title{left:30px;top:12px;width:350px;font-size:40px}
.back-title{left:0;top:16px;width:510px;font-size:46px}
.ribbon{position:absolute;left:382px;top:0;width:98px;height:106px}
.ribbon-text{position:absolute;left:382px;top:14px;width:98px;text-align:center;color:var(--ink);font-size:9px;line-height:1.2;font-weight:600}
.ribbon-text .abbr{display:block;font-size:15px;margin-bottom:4px}
.date{position:absolute;left:40px;top:90px;width:330px;text-align:center;font-size:16px;color:var(--maroon);font-weight:500;line-height:20px}
.venue{position:absolute;left:20px;top:112px;width:370px;text-align:center;font-size:10.5px;color:var(--ink);font-weight:500}
.band{position:absolute;left:0;top:137px;width:510px;height:93px;background:var(--maroon)}
.band-text{position:absolute;left:0;top:158px;width:348px;text-align:center;color:var(--cream);font-size:12.5px;line-height:16px}
.band-text .small{font-size:10px}
.pill{position:absolute;background:var(--pill);color:var(--cream);border-radius:5px;text-align:center;font-weight:500}
.pill--mats{left:134px;top:130px;width:74px;height:20px;background:#9d8a86;font-size:14px;line-height:20px;color:#fff;border-radius:4px}
.panel{position:absolute;left:0;width:348px;background:var(--brown);border-radius:0 10px 10px 0}
.panel--reg{top:230px;height:215px;background:linear-gradient(180deg,var(--brown),var(--brown-dark))}
.peach{position:absolute;left:0;width:510px;background:var(--peach)}
.peach--mid{top:445px;height:19px}
.peach--foot{top:702px;height:20px}
.panel--info{top:464px;height:238px;width:510px;border-radius:0;background:linear-gradient(180deg,#94643a,var(--brown))}
.reg{position:absolute;left:0;width:348px;text-align:center;color:var(--cream)}
.reg .tag{display:inline-block;background:var(--pill);padding:0 6px;border-radius:4px;font-size:14px;line-height:19px}
.reg .due{display:block;font-size:13.5px;line-height:18px;margin-top:1px}
.reg--early{top:240px}
.reg--regular{top:286px}
.reg--late{top:330px}
.limit{position:absolute;left:0;top:381px;width:348px;text-align:center;color:var(--cream);font-size:12px;line-height:15.5px}
.pill--weigh{left:120px;top:453px;width:92px;height:24px;font-size:16px;line-height:24px}
.info{position:absolute;left:22px;width:330px;text-align:center;color:var(--cream);font-size:7.5px;line-height:12.5px}
.info--times{top:482px;color:var(--peach);font-size:8px}
.info--rules{top:531px}
.info--awards{top:581px}
.admission{position:absolute;left:112px;top:625px;background:var(--pill);color:var(--cream);font-size:8px;padding:1px 5px;border-radius:2px}
.info--contact{top:642px}
.info--hotels{top:660px;color:var(--peach);font-size:7px}
.info--hotel-list{top:673px;font-size:8px}
.art{position:absolute}
.art--warrior-front{left:330px;top:120px;width:180px;height:602px;background:radial-gradient(ellipse at 55% 40%,#8c6a55 0%,#4c3226 45%,#2a1a14 80%);border-radius:50% 40% 0 0/20% 20% 0 0}
.table-box{position:absolute;left:17px;top:112px;width:472px;height:262px;background:linear-gradient(180deg,#8d5e31,#6d4322);border-radius:14px}
.weights{position:absolute;left:27px;top:122px;width:454px;font-size:4.6px;color:var(--table-line);text-align:center;line-height:1}
.weights-title{background:#160808;color:#fff;font-size:7.5px;height:14px;line-height:14px;border:1px solid var(--table-line)}
.weights-grid{display:grid;grid-template-columns:44fr 40fr 43fr 45fr 43fr 30fr 42fr 42fr 40fr 42fr 42fr}
.col{display:flex;flex-direction:column}
.cell{border:.5px solid var(--table-line);height:9.6px;line-height:9px}
.cell--num{background:var(--maroon);color:#fff;height:11px;line-height:11px;font-size:6px}
.cell--label{height:44px;display:flex;align-items:center;justify-content:center;padding:0 2px;line-height:1.25}
.art--mats{left:0;top:393px;width:510px;height:157px;background:linear-gradient(180deg,#a89a86,#6f6559 40%,#4a3f38)}
.bottom{position:absolute;left:0;top:550px;width:510px;height:172px;background:linear-gradient(180deg,var(--brown),#7a4e26)}
.singlet-note{position:absolute;left:110px;top:580px;width:266px;text-align:center;color:var(--cream);font-size:16.5px;line-height:26px}
.art--warrior-back{left:0;top:506px;width:96px;height:216px;background:radial-gradient(ellipse at 60% 35%,#8c6a55,#3a261c 70%);border-radius:40% 40% 0 0/25% 25% 0 0}
.art--singlets{left:380px;top:566px;width:124px;height:148px;background:linear-gradient(135deg,#6b1518 0%,#6b1518 50%,#d9c8a8 50%,#c9b592 100%);border-radius:10px}
</style>
</head>
<body>

<section class="page page--front" aria-label="Flyer page one">
  <h1 class="title front-title">8th Annual Ridgeback<br>Clash</h1>

  <svg class="ribbon" viewBox="0 0 98 106" aria-hidden="true"><polygon points="0,0 98,0 98,106 49,86 0,106" fill="var(--ribbon)"/></svg>
  <div class="ribbon-text"><span class="abbr">CPWA</span>Carolina Plains Wrestling Association</div>

  <p class="date">Saturday, January 24, 2026</p>
  <p class="venue">Harborview Event Center 118 Market Ridge Ave Fairhaven, NC</p>

  <div class="band"></div>
  <div class="art art--warrior-front" role="img" aria-label="Illustration of a helmeted warrior in red cape holding a spear"></div>
  <div class="pill pill--mats">6 Mats</div>
  <p class="band-text">
    K-5, 6U, 8U, 10U - Wrestling Starts at 8:30 AM<br>
    12U, Middle School &amp; High School , Open 18+<br>
    Wrestling Starts at 1:00 PM<br>
    <span class="small">Register @ www.matentryhub.com</span>
  </p>

  <div class="panel panel--reg"></div>
  <p class="reg reg--early"><span class="tag">Early Registration $25.00</span><span class="due">Deadline is January 18, 2026 at 11:59 PM</span></p>
  <p class="reg reg--regular"><span class="tag">Regular Registration is $35.00</span><span class="due">Deadline is January 21, 2026 at 11:59 PM</span></p>
  <p class="reg reg--late"><span class="tag">Late / On-site Registration is $50.00</span><span class="due">Deadline is January 23, 2026 at 5:00 PM</span></p>
  <p class="limit">Registration is limited to the first 750 wrestlers<br>Non-CPWA card holders will pay<br>an additional $5.00 at weigh-ins.</p>

  <div class="peach peach--mid"></div>
  <div class="panel panel--info"></div>
  <div class="peach peach--foot"></div>
  <div class="pill pill--weigh">Weigh-Ins</div>

  <p class="info info--times">
    January 23, 2026-5:00 PM to 7:00 PM ( Early weigh-ins - $10 cash due at scale)<br>
    January 24, 2026-6:00 AM to 7:30 AM ( K-5, 6U, 8U, 10U)<br>
    January 24, 2026-11:00 AM to 12:00 PM ( 12 &amp; under, MS, &amp; High School)
  </p>
  <p class="info info--rules">
    Tenths are waived/dropped at weigh-ins, satellite weigh-ins<br>
    will not be allowed, High School divisions are given 2 lbs. growth allowance,<br>
    Custom medals will be given to the top 3 individual finishers in each bracket .
  </p>
  <p class="info info--awards">
    Custom awards will be awarded to the top 4 teams, referee decisions<br>
    will be final, Pinecrest Athletics is not responsible for accidents,<br>
    injuries, or theft during the tournament.
  </p>
  <span class="admission">Admission : $10.00 per person</span>
  <p class="info info--contact">For more information, contact tournament director Dale Corbin : (555) 014-2290</p>
  <p class="info info--hotels">Hotels available on-site</p>
  <p class="info info--hotel-list">Riverside Suites (555) 014-5000 / Lakeview Lodge (555) 014-7400 / Parkway Inn (555) 014-8300</p>
</section>

<section class="page page--back" aria-label="Flyer page two">
  <h2 class="title back-title">8th Annual Ridgeback<br>Clash</h2>

  <div class="table-box"></div>
  <div class="weights">
    <div class="weights-title">2025–2026 CPWA Age &amp; Weight Classes</div>
    <div class="weights-grid">
      <div class="col">
        <div class="cell cell--num">Division</div>
        <div class="cell cell--label">Excluding the High School &amp; Open Division<br>12/31/2025</div>
        <div class="cell"></div><div class="cell"></div><div class="cell"></div><div class="cell"></div><div class="cell"></div><div class="cell"></div><div class="cell"></div>
      </div>
      <div class="col">
        <div class="cell cell--num">1</div><div class="cell cell--label">6 &amp; Under</div>
        <div class="cell">36</div><div class="cell">40</div><div class="cell">44</div><div class="cell">48</div><div class="cell">52</div><div class="cell">56</div><div class="cell">60</div><div class="cell">HWT</div>
      </div>
      <div class="col">
        <div class="cell cell--num">2</div><div class="cell cell--label">8 &amp; Under</div>
        <div class="cell">40</div><div class="cell">44</div><div class="cell">48</div><div class="cell">52</div><div class="cell">56</div><div class="cell">60</div><div class="cell">64</div><div class="cell">68</div><div class="cell">72</div><div class="cell">76</div><div class="cell">80</div><div class="cell">84</div><div class="cell">88</div><div class="cell">92</div><div class="cell">HWT</div>
      </div>
      <div class="col">
        <div class="cell cell--num">3</div><div class="cell cell--label">10 &amp; Under</div>
        <div class="cell">52</div><div class="cell">55</div><div class="cell">58</div><div class="cell">64</div><div class="cell">68</div><div class="cell">72</div><div class="cell">76</div><div class="cell">80</div><div class="cell">84</div><div class="cell">88</div><div class="cell">92</div><div class="cell">96</div><div class="cell">100</div><div class="cell">110</div><div class="cell">HWT</div>
      </div>
      <div class="col">
        <div class="cell cell--num">4</div><div class="cell cell--label">12 &amp; Under</div>
        <div class="cell">68</div><div class="cell">72</div><div class="cell">76</div><div class="cell">83</div><div class="cell">90</div><div class="cell">98</div><div class="cell">106</div><div class="cell">113</div><div class="cell">120</div><div class="cell">125</div><div class="cell">132</div><div class="cell">138</div><div class="cell">144</div><div class="cell">150</div><div class="cell">157</div><div class="cell">165</div><div class="cell">175</div><div class="cell">190</div><div class="cell">HWT</div>
      </div>
      <div class="col">
        <div class="cell cell--num">5</div><div class="cell cell--label">Middle School</div>
        <div class="cell">76</div><div class="cell">83</div><div class="cell">90</div><div class="cell">98</div><div class="cell">106</div><div class="cell">113</div><div class="cell">120</div><div class="cell">126</div><div class="cell">132</div><div class="cell">138</div><div class="cell">144</div><div class="cell">150</div><div class="cell">157</div><div class="cell">165</div><div class="cell">175</div><div class="cell">190</div><div class="cell">215</div><div class="cell">HW</div>
      </div>
      <div class="col">
        <div class="cell cell--num">6</div><div class="cell cell--label">Girls K-5</div>
        <div class="cell">40</div><div class="cell">44</div><div class="cell">48</div><div class="cell">52</div><div class="cell">56</div><div class="cell">60</div><div class="cell">64</div><div class="cell">68</div><div class="cell">72</div><div class="cell">76</div><div class="cell">80</div><div class="cell">84</div><div class="cell">88</div><div class="cell">92</div><div class="cell">95</div><div class="cell">100</div><div class="cell">110</div><div class="cell">120</div><div class="cell">130</div>
      </div>
      <div class="col">
        <div class="cell cell--num">7</div><div class="cell cell--label">Girls<br>6th - 8th</div>
        <div class="cell">76</div><div class="cell">83</div><div class="cell">90</div><div class="cell">98</div><div class="cell">106</div><div class="cell">113</div><div class="cell">120</div><div class="cell">126</div><div class="cell">132</div><div class="cell">138</div><div class="cell">144</div><div class="cell">150</div><div class="cell">157</div><div class="cell">165</div><div class="cell">175</div><div class="cell">190</div><div class="cell">215</div><div class="cell">HWT</div>
      </div>
      <div class="col">
        <div class="cell cell--num">8</div><div class="cell cell--label">Girls<br>9th - 12th</div>
        <div class="cell">100</div><div class="cell">107</div><div class="cell">114</div><div class="cell">120</div><div class="cell">126</div><div class="cell">132</div><div class="cell">145</div><div class="cell">152</div><div class="cell">165</div><div class="cell">185</div><div class="cell">235</div>
      </div>
      <div class="col">
        <div class="cell cell--num">9</div><div class="cell cell--label">Girls<br>9th - 12th</div>
        <div class="cell">106</div><div class="cell">113</div><div class="cell">120</div><div class="cell">126</div><div class="cell">132</div><div class="cell">138</div><div class="cell">144</div><div class="cell">150</div><div class="cell">157</div><div class="cell">165</div><div class="cell">175</div><div class="cell">190</div><div class="cell">215</div><div class="cell">285</div>
      </div>
      <div class="col">
        <div class="cell cell--num">10</div><div class="cell cell--label">Open 18+</div>
        <div class="cell">125</div><div class="cell">133</div><div class="cell">141</div><div class="cell">149</div><div class="cell">157</div><div class="cell">165</div><div class="cell">174</div><div class="cell">184</div><div class="cell">197</div><div class="cell">215</div><div class="cell">285</div>
      </div>
    </div>
  </div>

  <div class="art art--mats" role="img" aria-label="Aerial photo of six wrestling mats in an arena"></div>

  <div class="bottom"></div>
  <div class="art art--warrior-back" role="img" aria-label="Illustration of a helmeted warrior holding a spear"></div>
  <p class="singlet-note">Custom singlets are awarded<br>to champions in all weight<br>classes, excluding the High School<br>and Open Division.</p>
  <div class="art art--singlets" role="img" aria-label="Two custom tournament wrestling singlets in maroon and cream"></div>
</section>

</body>
</html>
```